Informational Chiropractic Brochure

We need an informational bi-fold brochure. It needs to include information about chiropractic, helpful for back pain, neck pain, migraines, etc. These brochures will be handed out at corporate chair massage events to encourage people to go beyond a massage and seek chiropractic for their musculoskeletal issues.

Target Market(s)

Men and Women, ages 25 to 50, business women

Font styles to use
Serif
Sans Serif

Colors
f37122
0355a3
85acd3

Requirements
Must have
• The least invasive treatment for back pain relief

```html
<!DOCTYPE html>
<html lang="en">
<head>
<meta charset="utf-8">
<title>Northbend Chiropractic – Bi-fold Brochure</title>
<link href="https://fonts.googleapis.com/css2?family=Archivo+Black&family=Lato:wght@400;700&family=Arimo:wght@400&display=swap" rel="stylesheet">
<style>
  :root{
    --navy:#1d3658;
    --white:#ffffff;
    --ink:#1d3658;
    --stage:#1e1e1e;
    --skin:#c9a894;
    --pink:#e9a9b4;
    --grey:#b9b9b9;
  }
  *{margin:0;padding:0;box-sizing:border-box}
  html,body{width:1200px;height:750px;overflow:hidden;background:var(--stage)}
  .canvas{position:relative;width:1200px;height:750px}
  .spread{position:absolute;top:175px;width:540px;height:400px;display:flex;box-shadow:0 10px 30px rgba(0,0,0,.5)}
  .spread--outside{left:45px}
  .spread--inside{left:615px}
  .panel{position:relative;width:270px;height:400px;overflow:hidden}
  .panel svg.shape{position:absolute;inset:0}
  .panel--navy{background:var(--navy)}
  .panel--white{background:var(--white)}
  .headline{position:absolute;left:14px;right:10px;font-family:"Archivo Black",sans-serif;color:var(--white);font-size:17px;letter-spacing:.5px;line-height:1}
  .body-copy{position:absolute;left:14px;right:12px;font-family:"Lato",sans-serif;color:var(--white);font-size:9.4px;line-height:1.36;text-align:justify}
  .back .headline{top:16px}
  .back .body-copy{top:42px}
  .photo-box{position:absolute}
  .back .photo-box{left:10px;right:10px;top:286px;height:104px;background:linear-gradient(120deg,#e9ecef,#a9bccd 55%,#d8d2cc)}
  .brand{position:absolute;left:22px;top:306px;display:flex;align-items:center;gap:10px}
  .brand-mark{width:40px;height:40px;border-radius:50%;border:2px solid var(--navy)}
  .brand-name{font-family:"Lato",sans-serif;font-weight:400;color:var(--ink);font-size:17px;line-height:1.1}
  .tagline{position:absolute;left:10px;right:10px;top:360px;text-align:center;font-family:"Arimo",sans-serif;color:var(--ink);font-size:14.5px;line-height:1.2}
  .inside-left .cover-line{position:absolute;right:18px;top:288px;width:220px;font-family:"Archivo Black",sans-serif;color:var(--white);font-size:17px;line-height:1.1;text-align:right;letter-spacing:.5px}
  .inside-right .headline{top:16px}
  .inside-right .body-copy{top:40px}
</style>
</head>
<body>
<div class="canvas">

  <section class="spread spread--outside">
    <article class="panel panel--navy back">
      <h2 class="headline">CUSTOM HEADING</h2>
      <p class="body-copy">Chiropractic care looks at the spine, joints and muscles as one system. Gentle adjustments restore motion, ease pressure on nerves and help the body heal on its own. Many patients find relief from back pain, neck pain, tension headaches and migraines without drugs or surgery. A massage relaxes tight muscles for a day; a chiropractic plan corrects the cause. Long hours at a desk, a heavy bag or poor sleep can pull the spine out of balance. Your first visit includes a full history, a posture check and a gentle exam, so your care fits your body and your schedule. Sessions are short and easy to fit into a work day. Book a short assessment and learn how small changes can keep you moving well.</p>
      <div class="photo-box" role="img" aria-label="Photo of a man leaning on a wall holding his lower back"></div>
    </article>

    <article class="panel panel--white cover">
      <svg class="shape" width="270" height="400" viewBox="0 0 270 400">
        <defs>
          <radialGradient id="spineGlow" cx="0.6" cy="0.4" r="0.7">
            <stop offset="0" stop-color="#8fb3cf"/>
            <stop offset="0.6" stop-color="#4f7898"/>
            <stop offset="1" stop-color="#dfe8ef"/>
          </radialGradient>
        </defs>
        <path d="M20 0 H270 V292 Q120 292 18 150 Z" fill="url(#spineGlow)" role="img" aria-label="Illustration of a man's back with the spine highlighted"/>
        <path d="M18 150 Q120 292 270 292" fill="none" stroke="var(--navy)" stroke-width="3"/>
      </svg>
      <div class="brand">
        <span class="brand-mark"></span>
        <span class="brand-name">Northbend<br>Chiropractic LLC</span>
      </div>
      <p class="tagline">The Least Invasive Treatment<br>for Back Pain Relief</p>
    </article>
  </section>

  <section class="spread spread--inside">
    <article class="panel panel--white inside-left">
      <svg class="shape" width="270" height="400" viewBox="0 0 270 400">
        <defs>
          <linearGradient id="backPhoto" x1="0" y1="0" x2="1" y2="1">
            <stop offset="0" stop-color="#dfe3e6"/>
            <stop offset="0.5" stop-color="var(--pink)"/>
            <stop offset="1" stop-color="var(--skin)"/>
          </linearGradient>
        </defs>
        <path d="M0 10 H262 V150 Q220 250 0 262 Z" fill="url(#backPhoto)" role="img" aria-label="Photo of a woman in a pink top holding her lower back"/>
        <path d="M0 278 Q200 275 270 160 V400 H0 Z" fill="var(--navy)"/>
        <path d="M0 272 Q196 270 270 155" fill="none" stroke="var(--white)" stroke-width="3"/>
      </svg>
      <p class="cover-line">THE LEAST INVASIVE TREATMENT FOR BACK PAIN RELIEF</p>
    </article>

    <article class="panel panel--navy inside-right">
      <svg class="shape" width="270" height="400" viewBox="0 0 270 400">
        <defs>
          <radialGradient id="neckPhoto" cx="0.45" cy="0.45" r="0.7">
            <stop offset="0" stop-color="#e5906a"/>
            <stop offset="0.45" stop-color="var(--grey)"/>
            <stop offset="1" stop-color="#f2f2f2"/>
          </radialGradient>
        </defs>
        <path d="M0 300 Q150 300 270 232 V400 H0 Z" fill="var(--white)"/>
        <rect x="70" y="258" width="190" height="132" fill="url(#neckPhoto)" role="img" aria-label="Photo of a man rubbing a painful neck"/>
      </svg>
      <h2 class="headline">CUSTOM HEADING</h2>
      <p class="body-copy">Back pain is one of the most common reasons people miss work. Most cases come from joints that do not move well and muscles that guard them. Chiropractic adjustments restore that motion by hand, with no needles, drugs or downtime. Care may also include stretches, posture tips and simple home exercises. Neck pain and migraines often share the same roots in the upper spine, so many patients see relief in both. We work with busy schedules and keep every visit short. Ask us how a plan can help you feel better at your desk and beyond.</p>
    </article>
  </section>

</div>
</body>
</html>
```